Flyer for Aluminium recycling business

We are a startup aluminium recycling business. We don’t have a logo yet. I’ve attached a flyer created by one of our sales people but it’s a bit average and we need something a bit more modern and slick. You have creative license to completely change everything - as long as the information being communicated is the same.

Target Market(s)

Hospitality, Hotels, Apartment blocks, malls etcs

Industry/Entity Type

Aluminium recycling

Requirements
Must have
• the wording
Nice to have
• you have free license on design aspect

```html
<!DOCTYPE html>
<html lang="en">
<head>
<meta charset="utf-8">
<title>Circular Reclaim – Aluminium Recycling Flyer</title>
<link rel="stylesheet" href="https://fonts.googleapis.com/css2?family=Poppins:wght@400;700;800&family=Roboto:wght@400&display=swap">
<style>
  :root {
    --backdrop: #808080;
    --paper: #ffffff;
    --forest: #283f3b;
    --ink: #2a3a37;
    --amber: #fbb81d;
  }
  * { box-sizing: border-box; margin: 0; padding: 0; }
  html, body { width: 1200px; height: 1200px; overflow: hidden; }
  body { background: var(--backdrop); position: relative; font-family: 'Roboto', sans-serif; color: var(--ink); }

  .flyer { position: absolute; left: 233px; top: 85px; width: 734px; height: 1030px; background: var(--paper); overflow: hidden; }
  .flyer__waves { position: absolute; inset: 0; width: 734px; height: 1030px; }

  .brand-title { position: absolute; top: 28px; left: 0; width: 100%; text-align: center;
    font-family: 'Poppins', sans-serif; font-weight: 800; font-size: 55px; letter-spacing: 1.5px; word-spacing: 6px;
    color: var(--forest); line-height: 1; }

  .slogan-pill { position: absolute; left: 42px; top: 118px; width: 650px; height: 39px; border-radius: 20px;
    background: var(--forest); color: var(--amber); font-family: 'Poppins', sans-serif; font-weight: 700;
    font-size: 21.5px; display: flex; align-items: center; justify-content: center; }

  .intro { position: absolute; top: 173px; left: 0; width: 100%; text-align: center; font-size: 18.5px; line-height: 23px; color: var(--ink); }

  .info-card { position: absolute; left: 61px; width: 611px; background: var(--paper); border-radius: 31px; }
  .info-card--steps { top: 288px; height: 269px; }
  .info-card--accepted { top: 579px; height: 314px; }

  .card-tab { position: absolute; top: 0; left: 50%; transform: translateX(-50%); }
  .card-tab svg { display: block; }
  .card-tab__label { position: absolute; inset: 0; display: flex; align-items: center; justify-content: center;
    font-family: 'Poppins', sans-serif; font-weight: 700; color: var(--forest); font-size: 22px; padding-bottom: 2px; }

  .check-list { position: absolute; left: 24px; right: 24px; list-style: none; }
  .info-card--steps .check-list { top: 52px; }
  .info-card--accepted .check-list { top: 62px; }
  .check-list li { position: relative; padding-left: 25px; font-size: 16.8px; line-height: 19.5px; color: var(--ink); }
  .info-card--steps li { margin-bottom: 10.5px; }
  .info-card--accepted li { margin-bottom: 10.5px; }
  .check-list li svg { position: absolute; left: 0; top: 3px; width: 14px; height: 14px; }

  .contact { position: absolute; left: 0; width: 100%; display: flex; justify-content: center; align-items: center; color: var(--forest); font-family: 'Poppins', sans-serif; }
  .contact--phone { top: 938px; font-weight: 700; font-size: 31px; gap: 10px; }
  .contact--email { top: 977px; font-weight: 400; font-size: 20px; gap: 14px; }
</style>
</head>
<body>
<main class="flyer">
  <svg class="flyer__waves" viewBox="0 0 734 1030" aria-hidden="true">
    <path fill="#fbb81d" d="M0 162 Q367 338 734 162 L734 194 Q367 308 0 194 Z"/>
    <path fill="#283f3b" d="M0 201 Q367 305 734 201 L734 986 Q367 858 0 986 Z"/>
    <path fill="#fbb81d" d="M0 993 Q367 853 734 993 L734 1014 Q367 836 0 1014 Z"/>
  </svg>

  <h1 class="brand-title">CIRCULAR RECLAIM</h1>
  <p class="slogan-pill">Playing the fair aluminium recycling game for good</p>
  <p class="intro">Our partnership with you is based on common sense,<br>mutual gain and a better tomorrow</p>

  <section class="info-card info-card--steps">
    <div class="card-tab">
      <svg width="178" height="41" viewBox="0 0 178 41"><path d="M1 0 L20 33 Q24 40 32 40 L146 40 Q154 40 158 33 L177 0" fill="#fbb81d" stroke="#283f3b" stroke-width="2"/></svg>
      <h2 class="card-tab__label">It's simple</h2>
    </div>
    <ul class="check-list">
      <li><svg viewBox="0 0 14 14"><circle cx="7" cy="7" r="7" fill="#283f3b"/><path d="M3.8 7.2 L6 9.3 L10.3 4.9" fill="none" stroke="#fff" stroke-width="1.8"/></svg>We bring you a free bin</li>
      <li><svg viewBox="0 0 14 14"><circle cx="7" cy="7" r="7" fill="#283f3b"/><path d="M3.8 7.2 L6 9.3 L10.3 4.9" fill="none" stroke="#fff" stroke-width="1.8"/></svg>You throw all and any aluminium waste into the bin - no need to super-clean it. Try to compact/squash the aluminium as much as possible</li>
      <li><svg viewBox="0 0 14 14"><circle cx="7" cy="7" r="7" fill="#283f3b"/><path d="M3.8 7.2 L6 9.3 L10.3 4.9" fill="none" stroke="#fff" stroke-width="1.8"/></svg>We collect the bin at no charge</li>
      <li><svg viewBox="0 0 14 14"><circle cx="7" cy="7" r="7" fill="#283f3b"/><path d="M3.8 7.2 L6 9.3 L10.3 4.9" fill="none" stroke="#fff" stroke-width="1.8"/></svg>We turn the aluminium waste into a desirable resource</li>
      <li><svg viewBox="0 0 14 14"><circle cx="7" cy="7" r="7" fill="#283f3b"/><path d="M3.8 7.2 L6 9.3 L10.3 4.9" fill="none" stroke="#fff" stroke-width="1.8"/></svg>We pay you for however much of that resource your waste has generated - and give you a report on that, so you can see how good you are</li>
    </ul>
  </section>

  <section class="info-card info-card--accepted">
    <div class="card-tab">
      <svg width="424" height="41" viewBox="0 0 424 41"><path d="M1 0 L20 33 Q24 40 32 40 L392 40 Q400 40 404 33 L423 0" fill="#fbb81d" stroke="#283f3b" stroke-width="2"/></svg>
      <h2 class="card-tab__label">Examples of what we can take</h2>
    </div>
    <ul class="check-list">
      <li><svg viewBox="0 0 14 14"><circle cx="7" cy="7" r="7" fill="#283f3b"/><path d="M3.8 7.2 L6 9.3 L10.3 4.9" fill="none" stroke="#fff" stroke-width="1.8"/></svg>Used beverage cans - any</li>
      <li><svg viewBox="0 0 14 14"><circle cx="7" cy="7" r="7" fill="#283f3b"/><path d="M3.8 7.2 L6 9.3 L10.3 4.9" fill="none" stroke="#fff" stroke-width="1.8"/></svg>Tinfoil-scrunched, crusty, burned or dirty</li>
      <li><svg viewBox="0 0 14 14"><circle cx="7" cy="7" r="7" fill="#283f3b"/><path d="M3.8 7.2 L6 9.3 L10.3 4.9" fill="none" stroke="#fff" stroke-width="1.8"/></svg>Disposable BBQ roasting trays</li>
      <li><svg viewBox="0 0 14 14"><circle cx="7" cy="7" r="7" fill="#283f3b"/><path d="M3.8 7.2 L6 9.3 L10.3 4.9" fill="none" stroke="#fff" stroke-width="1.8"/></svg>Aluminium takeaway containers</li>
      <li><svg viewBox="0 0 14 14"><circle cx="7" cy="7" r="7" fill="#283f3b"/><path d="M3.8 7.2 L6 9.3 L10.3 4.9" fill="none" stroke="#fff" stroke-width="1.8"/></svg>Wine bottle screw tops (and collars - if you can get them off)</li>
      <li><svg viewBox="0 0 14 14"><circle cx="7" cy="7" r="7" fill="#283f3b"/><path d="M3.8 7.2 L6 9.3 L10.3 4.9" fill="none" stroke="#fff" stroke-width="1.8"/></svg>Capsula (or any other aluminium) coffee pods</li>
      <li><svg viewBox="0 0 14 14"><circle cx="7" cy="7" r="7" fill="#283f3b"/><path d="M3.8 7.2 L6 9.3 L10.3 4.9" fill="none" stroke="#fff" stroke-width="1.8"/></svg>Tear-off can lids</li>
      <li><svg viewBox="0 0 14 14"><circle cx="7" cy="7" r="7" fill="#283f3b"/><path d="M3.8 7.2 L6 9.3 L10.3 4.9" fill="none" stroke="#fff" stroke-width="1.8"/></svg>Old/broken Slatepads, tablets, laptops or cell phones</li>
    </ul>
  </section>

  <p class="contact contact--phone">
    <svg width="25" height="25" viewBox="0 0 24 24" aria-hidden="true"><circle cx="12" cy="12" r="12" fill="#283f3b"/><path d="M8.2 5.5 L10 8.6 L8.8 10 Q10.3 13.3 13.9 15.2 L15.3 14 L18.4 15.8 L17.4 18 Q16.5 18.9 14.8 18.5 Q8.5 16.3 5.6 9.4 Q5.2 7.6 6.1 6.6 Z" fill="#fff"/></svg>
    020 555 0148
  </p>
  <p class="contact contact--email">
    <svg width="22" height="15" viewBox="0 0 22 15" aria-hidden="true"><rect width="22" height="15" rx="1" fill="#283f3b"/><path d="M1 1 L11 8.5 L21 1" fill="none" stroke="#fff" stroke-width="1.6"/></svg>
    join@circularreclaim.co.nz
  </p>
</main>
</body>
</html>
```